Growing Your Label eBook Cover Design

I want to deisgn a cover for my eBook (FRONT COVER) and the title is:

Why I Grew a Six-Figure Label. So You Should Start
By KL Baxter

TITLE CHANGED TO: OUT OF DEBT INTO POWER; WHY I GREW A NINE-FIGURE FORTUNE SO YOU SHOULD START

The color palette is attached. Along with some photos options of me. Along with the ebook in WORD Document. My website is www.KLBaXterHub.com. You can use a different color palette if you think it is best

Target Market(s)

women who look to build a personal brand

Industry/Entity Type

health and wellness

Requirements
Must have
• the title
Nice to have
• use my picture on the cover; but that is optional
Should not have
• any men

```html
<!DOCTYPE html>
<html lang="en">
<head>
<meta charset="utf-8">
<title>Out of Debt Into Power – eBook Cover</title>
<link rel="stylesheet" href="https://fonts.googleapis.com/css2?family=Red+Hat+Display:wght@400;700;800&family=Pacifico&family=Righteous&family=Dancing+Script:wght@500&display=swap">
<style>
  :root {
    --page-bg: #ffffff;
    --cover-pink: #eeaabb;
    --cover-pink-light: #f5c3cf;
    --maroon: #5e272c;
    --magenta: #d2117c;
    --brand-shadow: #7a5fa8;
    --band-pink: #e5869e;
    --url-pink: #f08fb0;
    --photo-deep: #8e3b4c;
    --photo-mid: #a2505f;
  }
  html, body {
    margin: 0;
    width: 1200px;
    height: 1000px;
    overflow: hidden;
    background: var(--page-bg);
  }
  .canvas {
    position: relative;
    width: 1200px;
    height: 1000px;
  }
  .cover {
    position: absolute;
    left: 278px;
    top: 44px;
    width: 646px;
    height: 913px;
    overflow: hidden;
    background: radial-gradient(ellipse 70% 55% at 50% 30%, var(--cover-pink-light), var(--cover-pink) 80%);
  }
  .title {
    position: absolute;
    left: 0;
    width: 100%;
    margin: 0;
    text-align: center;
    color: var(--maroon);
    white-space: nowrap;
  }
  .title-kicker {
    top: 56px;
    font: 700 26px/1 "Red Hat Display", sans-serif;
    letter-spacing: 1px;
    text-transform: uppercase;
  }
  .title-lead {
    top: 100px;
    font: 400 44px/1 "Red Hat Display", sans-serif;
  }
  .title-lead strong { font-weight: 800; }
  .title-script {
    top: 150px;
    font: 400 54px/1.2 "Pacifico", cursive;
  }
  .title-key {
    top: 238px;
    font: 400 84px/1 "Righteous", sans-serif;
    text-transform: uppercase;
    color: var(--magenta);
    text-shadow: 3px 4px 0 var(--brand-shadow);
    letter-spacing: 2px;
  }
  .title-tail {
    top: 322px;
    font: 400 34px/1 "Red Hat Display", sans-serif;
  }
  .title-tail strong { font-weight: 800; }
  .author-photo {
    position: absolute;
    left: 150px;
    top: 372px;
    width: 340px;
    height: 390px;
    background: radial-gradient(ellipse 50% 50% at 50% 45%, var(--photo-deep) 0%, var(--photo-mid) 50%, rgba(242,177,193,0) 100%);
  }
  .author-name {
    position: absolute;
    left: 0;
    top: 776px;
    width: 100%;
    text-align: center;
    margin: 0;
    font: 500 46px/1 "Dancing Script", cursive;
    color: var(--maroon);
  }
  .footer-bands {
    position: absolute;
    left: 0;
    bottom: 0;
    width: 646px;
    height: 100px;
  }
  .website {
    position: absolute;
    left: 0;
    bottom: 16px;
    width: 100%;
    margin: 0;
    text-align: center;
    font: 700 13px/1 "Red Hat Display", sans-serif;
    color: var(--url-pink);
    letter-spacing: 0.3px;
  }
</style>
</head>
<body>
<main class="canvas">
  <section class="cover">
    <p class="title title-kicker">Out of Debt Into Power;</p>
    <h1 class="title title-lead">Why I <strong>Grew</strong> a</h1>
    <p class="title title-script">Nine-Figure</p>
    <p class="title title-key">Fortune</p>
    <p class="title title-tail">So <strong>You Should Start</strong></p>

    <div class="author-photo" role="img" aria-label="Portrait photo of the author, KL Baxter, tinted in pink and maroon"></div>

    <p class="author-name">KL Baxter</p>

    <svg class="footer-bands" viewBox="0 0 646 100" preserveAspectRatio="none" aria-hidden="true">
      <path d="M0 24 Q323 2 646 24 L646 100 L0 100 Z" fill="var(--band-pink)"/>
      <rect x="0" y="36" width="646" height="64" fill="var(--maroon)"/>
    </svg>
    <p class="website">www.KLBaXterHub.com</p>
  </section>
</main>
</body>
</html>
```